Business Card Design

I am a Special Event Consultant,I arrange and organise Special Events - Product Launches,Sponsorship and Product Displays.

I would like the RTV to be a feature of the design with 'Special Event Services" underneath - keep it very simple but creative using this information. So it is just the letters "RTV" with Event Services underneath.

(Simple Colours - Silver, Black, Grey - no bright colours - We work for Valtoria Drenn,KDX, Lyndrel So it is class and classic.)

Only my Name and mobile on the front.

Contact Information for Business Card

FRONT
Tess Varnholt
Tel: 0436 218907

BACK
Email: tess@rtveventservices.example.au

2807 Wexbury Heights,83 Pollard Street
NORTHVALE.Vic.3158.

```html
<!DOCTYPE html>
<html lang="en">
<head>
<meta charset="UTF-8">
<title>RTV Special Event Services – Business Card</title>
<link rel="stylesheet" href="https://fonts.googleapis.com/css2?family=Source+Sans+3:wght@400&display=swap">
<style>
  :root {
    --ink: #000000;
    --stripe-black: #000000;
    --stripe-silver: #c4c8ca;
    --stripe-grey: #869798;
    --paper: #ffffff;
  }
  html, body {
    margin: 0;
    padding: 0;
    width: 935px;
    height: 1200px;
    overflow: hidden;
    background: var(--paper);
  }
  .sheet {
    position: relative;
    width: 935px;
    height: 1200px;
    font-family: "Source Sans 3", "Source Sans Pro", sans-serif;
    color: var(--ink);
  }
  .stripes {
    position: absolute;
    left: 0;
    width: 206px;
    display: flex;
  }
  .stripes--front { top: 0; height: 566px; }
  .stripes--back { top: 635px; height: 565px; }
  .stripe { flex: 1; }
  .stripe--black { background: var(--stripe-black); }
  .stripe--silver { background: var(--stripe-silver); }
  .stripe--grey { background: var(--stripe-grey); }

  .line {
    position: absolute;
    margin: 0;
    line-height: 1;
    white-space: nowrap;
    transform: translateX(-50%);
    font-weight: 400;
  }
  .holder-name { left: 529px; top: 207px; font-size: 68px; }
  .holder-phone { left: 529px; top: 280px; font-size: 33px; }
  .brand-mark { left: 555px; top: 753px; font-size: 55px; }
  .brand-tagline { left: 555px; top: 827px; font-size: 55px; }
  .contact-email { left: 555px; top: 928px; font-size: 36px; }
  .contact-address-1 { left: 548px; top: 1002px; font-size: 35px; }
  .contact-address-2 { left: 548px; top: 1047px; font-size: 35px; }
</style>
</head>
<body>
<main class="sheet">
  <section class="card card--front">
    <div class="stripes stripes--front">
      <span class="stripe stripe--black"></span>
      <span class="stripe stripe--silver"></span>
      <span class="stripe stripe--grey"></span>
      <span class="stripe stripe--black"></span>
      <span class="stripe stripe--silver"></span>
      <span class="stripe stripe--grey"></span>
    </div>
    <h1 class="line holder-name">Tess Varnholt</h1>
    <p class="line holder-phone">Tel: 0436 218907</p>
  </section>

  <section class="card card--back">
    <div class="stripes stripes--back">
      <span class="stripe stripe--black"></span>
      <span class="stripe stripe--silver"></span>
      <span class="stripe stripe--grey"></span>
      <span class="stripe stripe--black"></span>
      <span class="stripe stripe--silver"></span>
      <span class="stripe stripe--grey"></span>
    </div>
    <h2 class="line brand-mark">RTV</h2>
    <p class="line brand-tagline">Special Event Services</p>
    <p class="line contact-email">Email: tess@rtveventservices.example.au</p>
    <p class="line contact-address-1">2807 Wexbury Heights</p>
    <p class="line contact-address-2">83 Pollard Street NORTHVALE.Vic.3158</p>
  </section>
</main>
</body>
</html>
```